Create a landing page for my local business that I’m looking to advertise

I own an oriental rug repair, restoration and cleaning business.
I’m looking to rug advertising and i would like a very clear *******UX and UI design******* website designed.

pages that i need:
-Repair and restoration
-Cleaning
-Blocking
-Staircase rug installation
_about us
-homepage
-our story
-contact us
-estimate

Www.velborugs.example

Industry/Entity Type

Rug Industry, Antique and New Rug Repair restoration and cleaning

Number of Pages Required

5+ page

Font styles to use
Serif
Sans Serif
Script

Colors
6B429C
8869AF
B7A5CE
E3DAEB
F3F0F8

Requirements
Must have
• IT HAS TO PRESENT FINE RUG REPAIR, RESTORATION AND CLEANING.
Should not have
• I DONT WANT THE WEBSITE TO LOOK LIKE A GENERIC “CLEANING COMPANY”. WE ARE A HIGH END RUG REPAIR ,RESTORATION AND CLEANING COMPANY

```html
<!DOCTYPE html>
<html lang="en">
<head>
<meta charset="utf-8">
<title>Velbo Rugs — Oriental Rug Repair, Restoration &amp; Cleaning</title>
<link href="https://fonts.googleapis.com/css2?family=Libre+Baskerville:wght@400;700&family=Poppins:wght@300;400;500&family=Rubik:wght@700;800&display=swap" rel="stylesheet">
<style>
  :root{
    --gold:#C9A02C;
    --gold-dark:#B38C1F;
    --brown:#4A3F36;
    --brown-deep:#3B322B;
    --cream:#F5EEDF;
    --ink:#3A332D;
    --muted:#6E6660;
    --line:#CFC8C0;
    --white:#FFFFFF;
  }
  *{margin:0;padding:0;box-sizing:border-box}
  html,body{width:1200px;height:4172px;overflow:hidden}
  body{position:relative;background:var(--white);font-family:"Poppins",sans-serif;color:var(--ink)}
  .abs{position:absolute}
  .serif{font-family:"Libre Baskerville",serif}
  .btn{position:absolute;display:flex;align-items:center;justify-content:center;border-radius:30px;font-family:"Libre Baskerville",serif;font-weight:700;font-size:15px;color:var(--white);background:var(--gold);letter-spacing:.3px;white-space:nowrap}
  .btn.dark{background:var(--brown)}

  /* top bar + header */
  .topbar{left:0;top:0;width:1200px;height:32px;background:var(--gold)}
  .topbar .call{position:absolute;left:764px;top:10px;font-size:11px;color:#fff}
  .topbar .phone-dot{position:absolute;left:836px;top:2px;width:32px;height:32px;border-radius:50%;background:var(--brown);display:flex;align-items:center;justify-content:center}
  .topbar .num{position:absolute;left:884px;top:6px;font-family:"Libre Baskerville",serif;font-size:15px;color:#fff}
  .topbar .soc{position:absolute;top:4px;width:24px;height:24px;border:1.5px solid #fff;border-radius:50%}
  .brand-mark{left:68px;top:13px;width:92px;height:92px;border-radius:50%;background:#fff;border:2px solid var(--brown);display:flex;align-items:center;justify-content:center;text-align:center;font-family:"Libre Baskerville",serif;font-size:15px;font-weight:700;color:var(--brown);line-height:1.15;z-index:3}
  .nav{left:259px;top:69px;display:flex;gap:15px;font-size:10.5px;color:var(--ink);white-space:nowrap}
  .nav .on{color:var(--gold);border-bottom:2px solid var(--gold);padding-bottom:6px}
  .head-cta{left:976px;top:55px;width:224px;height:42px;background:var(--brown);border-radius:24px 0 0 24px;color:#fff;font-family:"Libre Baskerville",serif;font-size:16px;display:flex;align-items:center;padding-left:30px;white-space:nowrap}

  /* hero */
  .hero{left:0;top:117px;width:1200px;height:547px}
  .hero h1{position:absolute;left:123px;top:141px;font-family:"Rubik",sans-serif;font-weight:800;font-size:64px;line-height:64px;color:#fff}
  .hero .tag{position:absolute;left:122px;top:279px;font-family:"Libre Baskerville",serif;font-size:22px;color:var(--gold);white-space:nowrap}
  .arrow{position:absolute;top:326px;width:40px;height:40px;border-radius:50%;background:rgba(60,50,40,.55);display:flex;align-items:center;justify-content:center}

  .svc-icon{position:absolute;width:102px;height:102px;border-radius:50%;background:#fff;border:2px solid var(--brown);display:flex;align-items:center;justify-content:center}
  .svc-label{position:absolute;font-family:"Libre Baskerville",serif;font-size:15px;color:var(--ink);width:200px;text-align:center}

  /* welcome */
  .eyebrow{font-size:13px;color:var(--ink)}
  .welcome p{font-size:11.5px;line-height:21px;color:var(--muted)}

  /* services */
  .section-title{font-family:"Libre Baskerville",serif;font-weight:700;font-size:34px;color:var(--brown);text-align:center}
  .card{position:absolute;top:1549px;width:248px;height:313px;background:#fff;border-radius:4px;box-shadow:0 2px 10px rgba(0,0,0,.06)}
  .card .photo{position:absolute;left:6px;top:8px;width:236px;height:162px}
  .card h3{position:absolute;top:196px;width:100%;text-align:center;font-family:"Libre Baskerville",serif;font-weight:700;font-size:16px;color:var(--ink);white-space:nowrap}
  .card p{position:absolute;top:228px;left:20px;right:20px;text-align:center;font-size:11.5px;line-height:20px;color:var(--muted)}
  .card .btn{top:292px;left:57px;width:134px;height:36px;font-size:13px}

  .care-title{font-family:"Libre Baskerville",serif;font-weight:700;font-size:30px;line-height:40px;white-space:nowrap}
  .body-text{font-size:11.5px;line-height:21px;color:var(--muted)}

  .field{position:absolute;border:1px solid var(--line);border-radius:10px;font-size:11px;color:var(--muted);padding:12px 16px}

  /* footer */
  .foot-h{position:absolute;top:3870px;font-family:"Libre Baskerville",serif;font-weight:700;font-size:14px;color:var(--gold)}
  .foot-list{position:absolute;top:3906px;list-style:none;font-size:11.5px;color:#fff}
  .foot-list li{height:24px;display:flex;align-items:center}
  .foot-list li::before{content:"";width:4px;height:4px;border-radius:50%;background:var(--gold);margin-right:16px}
  .contact-row{position:absolute;left:604px;display:flex;gap:16px;font-size:11.5px;color:#fff;line-height:19px}
  .contact-row svg{flex:none}
  .copy{left:0;top:4124px;width:1200px;height:48px;background:var(--gold);color:#fff;font-size:11px;display:flex;align-items:center;justify-content:center}
</style>
</head>
<body>

<!-- top bar -->
<div class="abs topbar">
  <span class="call">Call Us On :</span>
  <span class="phone-dot"><svg width="16" height="16" viewBox="0 0 24 24"><path d="M6.6 10.8c1.4 2.8 3.8 5.1 6.6 6.6l2.2-2.2c.3-.3.7-.4 1-.2 1.1.4 2.3.6 3.6.6.6 0 1 .4 1 1V20c0 .6-.4 1-1 1C10.6 21 3 13.4 3 4c0-.6.4-1 1-1h3.5c.6 0 1 .4 1 1 0 1.3.2 2.5.6 3.6.1.3 0 .7-.2 1z" fill="#fff"/></svg></span>
  <span class="num">(555) 014-2290</span>
  <span class="soc" style="left:1023px"></span>
  <span class="soc" style="left:1053px"></span>
  <span class="soc" style="left:1083px"></span>
  <span class="soc" style="left:1113px"></span>
</div>

<!-- header -->
<div class="abs brand-mark">Velbo<br>Rugs</div>
<nav class="abs nav">
  <span class="on">Home</span><span>Repair &amp; Restoration</span><span>Cleaning</span><span>Blocking</span><span>Staircase Rug Installation</span><span>About Us</span><span>Our Story</span><span>Contact Us</span>
</nav>
<div class="abs head-cta">Get Free Estimate</div>

<!-- hero -->
<div class="abs hero">
  <svg width="1200" height="547" role="img" aria-label="Photo of a patterned grey area rug in a living room with a small dog sitting on it">
    <defs>
      <linearGradient id="heroGrad" x1="0" y1="0" x2="1" y2="1">
        <stop offset="0" stop-color="#7A5A3A"/>
        <stop offset=".45" stop-color="#A9A49C"/>
        <stop offset=".75" stop-color="#8C7F70"/>
        <stop offset="1" stop-color="#B08540"/>
      </linearGradient>
    </defs>
    <path d="M0 0H1200V433Q600 661 0 433Z" fill="url(#heroGrad)"/>
  </svg>
  <h1>Oriental Rug<br>Repair</h1>
  <div class="tag">Authenticity And Perfection.</div>
</div>
<div class="btn" style="left:121px;top:440px;width:232px;height:41px">GET A FREE ESTIMATE</div>
<div class="arrow" style="left:40px"><svg width="12" height="14"><path d="M9 1L3 7l6 6" stroke="#fff" stroke-width="1.5" fill="none"/></svg></div>
<div class="arrow" style="left:1120px"><svg width="12" height="14"><path d="M3 1l6 6-6 6" stroke="#fff" stroke-width="1.5" fill="none"/></svg></div>

<!-- service icons -->
<div class="svc-icon" style="left:276px;top:639px">
  <svg width="56" height="48" viewBox="0 0 56 48"><rect x="22" y="8" width="28" height="32" fill="none" stroke="#4A3F36" stroke-width="2"/><rect x="28" y="14" width="16" height="20" fill="#C9A02C"/><circle cx="10" cy="34" r="4" fill="none" stroke="#4A3F36" stroke-width="2"/><circle cx="18" cy="38" r="4" fill="none" stroke="#4A3F36" stroke-width="2"/><path d="M12 31L24 12M16 35L28 22" stroke="#4A3F36" stroke-width="2"/></svg>
</div>
<div class="svc-label" style="left:227px;top:760px">RUG REPAIR</div>
<div class="svc-icon" style="left:548px;top:661px">
  <svg width="56" height="48" viewBox="0 0 56 48"><rect x="10" y="6" width="36" height="36" fill="none" stroke="#4A3F36" stroke-width="2"/><rect x="22" y="10" width="22" height="28" fill="#C9A02C"/><path d="M10 12h-4M10 18h-4M10 24h-4M10 30h-4M10 36h-4M46 12h4M46 18h4M46 24h4M46 30h4M46 36h4" stroke="#4A3F36" stroke-width="2"/></svg>
</div>
<div class="svc-label" style="left:499px;top:783px">RESTORATION</div>
<div class="svc-icon" style="left:815px;top:639px">
  <svg width="56" height="48" viewBox="0 0 56 48"><path d="M8 10h36v30H8z" fill="none" stroke="#4A3F36" stroke-width="2"/><path d="M16 16l20 18M36 16L16 34" stroke="#C9A02C" stroke-width="5"/><ellipse cx="44" cy="10" rx="5" ry="5" fill="none" stroke="#4A3F36" stroke-width="2"/></svg>
</div>
<div class="svc-label" style="left:766px;top:760px">CLEANING</div>

<!-- welcome -->
<div class="abs welcome" style="left:136px;top:886px;width:410px">
  <div class="eyebrow">Welcome To</div>
  <div class="serif" style="font-weight:700;font-size:34px;color:var(--brown);margin-top:8px">Velborugs</div>
  <div class="serif" style="font-size:15px;color:var(--gold);margin-top:20px">30+ Years of Experience In Rug Restoration Field</div>
  <p style="margin-top:16px">Velbo Rugs is a leading and trusted brand for all oriental and antique rug repairs, not only by consumers, but by all Chicagoland's finest Oriental Rug dealers and designers. With more than 30-plus years of experience, we are proud to offer a wide range of services for all types of rugs, including fine Persian rugs, Afghan rugs, Pakistani rugs, wool rugs, Antique Rugs, Oriental Rugs, Shag and many others across the United States and all over the world.</p>
  <p style="margin-top:12px">Our repair, restoration and cleaning team specializes in high-quality antique rug restoration and repair, as well as wool &amp; silk rugs, from all over the world. Sometimes wear and tear can happen in high traffic areas, or can be damaged by your beloved dogs or cats..</p>
</div>
<div class="btn" style="left:134px;top:1268px;width:158px;height:39px">LEARN MORE</div>

<div class="abs" style="left:677px;top:912px;width:378px;height:378px;border-radius:50%;border:2px solid var(--brown);padding:10px">
  <div role="img" aria-label="Photo of an oriental rug on a wooden floor being cleaned with a vacuum" style="width:100%;height:100%;border-radius:50%;background:linear-gradient(135deg,#C9A36A 0%,#A0392E 45%,#1F2D5A 75%,#C9A36A 100%)"></div>
</div>
<div class="abs" style="left:665px;top:1170px;width:120px;height:120px;border-radius:50%;background:var(--gold);color:#fff;text-align:center;font-family:'Libre Baskerville',serif">
  <div style="font-size:38px;margin-top:20px;line-height:1">30+</div>
  <div style="font-size:18px;margin-top:8px">Years</div>
</div>

<!-- services -->
<svg class="abs" style="left:0;top:1373px" width="1200" height="581"><path d="M0 132Q600 -132 1200 132V581H0Z" fill="var(--cream)"/></svg>
<div class="abs eyebrow" style="left:0;top:1446px;width:1200px;text-align:center">What We Do</div>
<div class="abs section-title" style="left:0;top:1468px;width:1200px">Our Services</div>

<div class="card" style="left:71px">
  <div class="photo" role="img" aria-label="Photo of hands repairing the edge of a red oriental rug" style="background:linear-gradient(135deg,#8A2F22,#C08A5A 55%,#5A2A20)"></div>
  <h3>Repair And Restoration</h3>
  <p>Our Antique Rug Repair can help you improve your customer.</p>
  <div class="btn" style="background:var(--gold)">LEARN MORE</div>
</div>
<div class="card" style="left:342px">
  <div class="photo" role="img" aria-label="Photo of a red rug being cleaned with a hose" style="background:linear-gradient(135deg,#E9E6E0,#9A2A3A 55%,#3A2A40)"></div>
  <h3>Cleaning</h3>
  <p>Our Antique Rug Repair can help you improve your customer.</p>
  <div class="btn dark">LEARN MORE</div>
</div>
<div class="card" style="left:610px">
  <div class="photo" role="img" aria-label="Photo of a grey patterned rug laid out for blocking" style="background:linear-gradient(135deg,#9C8E7C,#6E6A66 50%,#B0A89A)"></div>
  <h3>Blocking</h3>
  <p>Our Antique Rug Repair can help you improve your customer.</p>
  <div class="btn dark">LEARN MORE</div>
</div>
<div class="card" style="left:881px">
  <div class="photo" role="img" aria-label="Photo of a patterned runner installed on a staircase" style="background:linear-gradient(135deg,#EDE9E2,#5A2A28 50%,#2B1E22)"></div>
  <h3>Staircase Rug Installation</h3>
  <p>Our Antique Rug Repair can help you improve your customer.</p>
  <div class="btn dark">LEARN MORE</div>
</div>

<!-- care -->
<div class="abs care-title" style="left:125px;top:2024px">
  <div style="color:var(--gold)">We Care And Respect</div>
  <div style="color:var(--brown)">The Rugs We Work On.</div>
</div>
<p class="abs body-text" style="left:601px;top:2028px;width:478px">With over 30 years of expertise in restoring and cleaning precious rugs, we feel we have a duty to bring each rug to its former glory whenever this is possible. We are a family-owned and -operated area rug repair and restoration firm near Chicago, specializing in Oriental Rug Cleaning, Antique Rug Repair, Sun Fade Damage, Rug Stain Removal and many more services. We use the best cleaning solutions for our hand-wash services, as well as wool and silk rugs.</p>

<div class="abs" style="left:329px;top:2236px;width:712px;height:358px;background:repeating-linear-gradient(45deg,var(--gold) 0 2px,#F3E6C0 2px 5px)"></div>
<div class="abs" role="img" aria-label="Photo of a workshop with rows of colored wool yarn on the wall and rugs on the floor" style="left:358px;top:2205px;width:712px;height:358px;background:linear-gradient(180deg,#F2F2F0 0%,#E4E2DE 40%,#9A6A4A 60%,#5A3A3A 80%,#7A5A48 100%)"></div>
<div class="abs" style="left:228px;top:2498px;width:266px;height:65px;background:var(--gold);color:#fff;font-family:'Libre Baskerville',serif;font-size:17px;display:flex;align-items:center;padding-left:45px;gap:20px;white-space:nowrap">LEARN MORE
  <svg width="30" height="10"><path d="M0 5h28M23 1l5 4-5 4" stroke="#fff" stroke-width="1.2" fill="none"/></svg>
</div>

<div class="abs serif" style="left:0;top:2664px;width:1200px;text-align:center;font-weight:700;font-size:27px;line-height:38px;color:var(--brown)">Antique Rug Repair, Oriental Rug Restoration<br>Antique Rug Cleaning</div>
<div class="btn" style="left:481px;top:2765px;width:236px;height:38px">GET A FREE ESTIMATE</div>

<!-- original -->
<div class="abs" style="left:0;top:2913px;width:1200px;height:361px;background:var(--brown)"></div>
<div class="abs" role="img" aria-label="Photo of a curved staircase with a patterned oriental runner" style="left:0;top:2872px;width:602px;height:442px;border-radius:0 50% 50% 0/0 50% 50% 0;background:linear-gradient(135deg,#C88A3A 0%,#6A3A22 40%,#3A2218 70%,#A06A30 100%)"></div>
<div class="abs" style="left:458px;top:3198px;width:84px;height:84px;border-radius:50%;background:#fff;border:4px solid #2E5A8A"></div>
<div class="abs care-title" style="left:644px;top:2968px;font-size:30px">
  <div style="color:var(--gold)">There Is Nothing More</div>
  <div style="color:#fff">Precious Than The Original.</div>
</div>
<p class="abs body-text" style="left:645px;top:3057px;width:480px;color:#E8E2DA">We value authenticity and we built our name on restoring rugs by hand, bringing back to life and using pieces that are in your family for generations or that you invested in because you appreciate their craftsmanship. This is our contribution to keeping the authenticity in your homes, and teaching new generations about the value manual craftsmanship can build, to the state of calling it art.</p>
<div class="btn" style="left:643px;top:3178px;width:235px;height:41px">GET A FREE ESTIMATE</div>

<!-- contact -->
<div class="abs serif" style="left:0;top:3378px;width:1200px;text-align:center;font-weight:700;font-size:30px"><span style="color:var(--gold)">Contact</span> <span style="color:var(--brown)">Us</span></div>
<div class="field" style="left:259px;top:3449px;width:306px;height:40px">Name *</div>
<div class="field" style="left:259px;top:3500px;width:306px;height:40px">Email *</div>
<div class="field" style="left:259px;top:3551px;width:306px;height:40px">Phone *</div>
<div class="field" style="left:581px;top:3449px;width:360px;height:142px">What can we help you with? *</div>
<div class="abs" style="left:266px;top:3604px;font-size:11px;color:var(--ink)">May we email you about this?*</div>
<div class="field" style="left:259px;top:3631px;width:682px;height:41px;display:flex;justify-content:space-between;align-items:center;padding-top:0;padding-bottom:0">-Select- *
  <svg width="12" height="8"><path d="M1 1l5 5 5-5z" fill="#4A3F36"/></svg>
</div>
<div class="btn" style="left:542px;top:3688px;width:114px;height:39px">SUBMIT</div>

<!-- footer -->
<svg class="abs" style="left:0;top:3803px" width="1200" height="321"><path d="M0 131Q600 -131 1200 131V321H0Z" fill="var(--brown-deep)"/></svg>
<div class="abs" style="left:126px;top:3906px;width:114px;height:114px;border-radius:50%;border:2px solid #fff;display:flex;align-items:center;justify-content:center;text-align:center;font-family:'Libre Baskerville',serif;font-weight:700;font-size:17px;color:#fff;line-height:1.2">Velbo<br>Rugs</div>
<div class="abs" style="left:112px;top:4035px;width:32px;height:32px;border-radius:50%;background:var(--gold)"></div>
<div class="abs" style="left:151px;top:4035px;width:32px;height:32px;border-radius:50%;background:var(--gold)"></div>
<div class="abs" style="left:190px;top:4035px;width:32px;height:32px;border-radius:50%;background:var(--gold)"></div>
<div class="abs" style="left:227px;top:4035px;width:32px;height:32px;border-radius:50%;background:var(--gold)"></div>

<div class="foot-h" style="left:337px">SITEMAP</div>
<ul class="foot-list" style="left:337px"><li>Home</li><li>Services</li><li>About us</li><li>Our story</li><li>Contact us</li><li>Estimate</li></ul>

<div class="foot-h" style="left:604px">CONTACT US</div>
<div class="contact-row" style="top:3906px">
  <svg width="18" height="22" viewBox="0 0 18 22"><path d="M9 1a7 7 0 0 0-7 7c0 5 7 13 7 13s7-8 7-13a7 7 0 0 0-7-7z" fill="none" stroke="#C9A02C" stroke-width="2"/><circle cx="9" cy="8" r="2.5" fill="#C9A02C"/></svg>
  <span>1420 Fernhill Ave,<br>Marlow, IL 60000</span>
</div>
<div class="contact-row" style="top:3960px">
  <svg width="18" height="18" viewBox="0 0 24 24"><path d="M6.6 10.8c1.4 2.8 3.8 5.1 6.6 6.6l2.2-2.2c.3-.3.7-.4 1-.2 1.1.4 2.3.6 3.6.6.6 0 1 .4 1 1V20c0 .6-.4 1-1 1C10.6 21 3 13.4 3 4c0-.6.4-1 1-1h3.5c.6 0 1 .4 1 1 0 1.3.2 2.5.6 3.6.1.3 0 .7-.2 1z" fill="#C9A02C"/></svg>
  <span>(555) 014-2290</span>
</div>
<div class="contact-row" style="top:3994px">
  <svg width="18" height="14" viewBox="0 0 18 14"><rect x="0" y="0" width="18" height="14" rx="1" fill="#C9A02C"/><path d="M1 1l8 6 8-6" stroke="#3B322B" stroke-width="1.5" fill="none"/></svg>
  <span>info@velborugs.example</span>
</div>
<div class="contact-row" style="top:4030px">
  <svg width="18" height="18" viewBox="0 0 18 18"><circle cx="9" cy="9" r="8" fill="none" stroke="#C9A02C" stroke-width="1.6"/><path d="M9 4v5l3 2" stroke="#C9A02C" stroke-width="1.6" fill="none"/></svg>
  <span>Monday - Friday 10AM – 5PM<br>Saturday 10AM – 1PM<br>Sunday - <span style="color:var(--gold)">Closed</span></span>
</div>

<div class="foot-h" style="left:887px">QUICK LINKS</div>
<ul class="foot-list" style="left:887px"><li>Blog</li><li>Privacy Policy</li><li>Shipping</li><li>Return Policy</li><li>Terms of Service</li><li>Contact Us</li></ul>

<div class="abs copy">©2021 Velbo Rugs - All rights reserved</div>

</body>
</html>
```